Business Card Design

my company buys cars,boats and caravans off the public, and also assists the public in helping them sell there item(brokering),i have an idea of a logo which is.....T$A....THE S BEING A LARGE DOLLAR SIGN,centred. And underneath my business name....TRADER-HOLDER-AGENT,i like black backgrounds, CLEAN SHARP AND TO THE POINT!!

Industry/Entity Type

Business

Contact Information for Business Card

$wap NOWLY.........buyer,seller,broker......cars,boats,caravans...........0427591846.......-swapnowly@traderholderagent.com.au, lmct-58417

Requirements
Must have
• MOBILE NUMBER-0427591846
EMAIL-swapnowly@traderholderagent.com.au
business name-TRADER-HOLDER-AGENT
lmct-58417
what we deal in-Cars,Caravans,Boats
cash,bank chq, finance paid out
Nice to have
• clever logo created by you guys

```html
<!DOCTYPE html>
<html lang="en">
<head>
<meta charset="utf-8">
<title>TRADER-HOLDER-AGENT — Business Card</title>
<link rel="stylesheet" href="https://fonts.googleapis.com/css2?family=Oswald:wght@300;400;600&display=swap">
<style>
  :root {
    --backdrop: #2a2a2a;
    --card-black: #0c0c0c;
    --brand-cyan: #3fb3c1;
    --accent-orange: #f0a23c;
    --band-cyan: #2fa3ad;
    --band-text: #0c0c0c;
  }
  * { margin: 0; padding: 0; box-sizing: border-box; }
  html, body {
    width: 1200px;
    height: 1000px;
    overflow: hidden;
    background: var(--backdrop);
  }
  .canvas {
    position: relative;
    width: 1200px;
    height: 1000px;
    display: flex;
    align-items: center;
    justify-content: center;
  }
  .business-card {
    position: relative;
    width: 900px;
    height: 514px;
    background: var(--card-black);
    border-radius: 22px;
    overflow: hidden;
    font-family: "Oswald", sans-serif;
  }
  .brand-row {
    position: absolute;
    left: 90px;
    top: 100px;
    display: flex;
    align-items: center;
    gap: 28px;
  }
  .brand-square {
    width: 96px;
    height: 96px;
    background: var(--brand-cyan);
    flex: none;
  }
  .brand-text {
    display: flex;
    flex-direction: column;
    gap: 2px;
  }
  .brand-name {
    font-size: 50px;
    font-weight: 600;
    line-height: 1.05;
    color: var(--brand-cyan);
    letter-spacing: 1px;
  }
  .brand-trades {
    font-size: 33px;
    font-weight: 300;
    line-height: 1.1;
    color: var(--accent-orange);
    letter-spacing: 7px;
  }
  .contact-block {
    position: absolute;
    left: 0;
    right: 0;
    top: 262px;
    text-align: center;
    color: var(--accent-orange);
    font-size: 26px;
    font-weight: 300;
    line-height: 1.5;
    letter-spacing: 1px;
  }
  .stripe-orange {
    position: absolute;
    left: 0;
    right: 0;
    bottom: 74px;
    height: 9px;
    background: var(--accent-orange);
  }
  .stripe-cyan {
    position: absolute;
    left: 0;
    right: 0;
    bottom: 0;
    height: 62px;
    background: var(--band-cyan);
    display: flex;
    align-items: center;
    justify-content: center;
  }
  .payment-terms {
    color: var(--band-text);
    font-size: 24px;
    font-weight: 400;
    letter-spacing: 3px;
    text-transform: uppercase;
  }
</style>
</head>
<body>
  <main class="canvas">
    <section class="business-card" aria-label="TRADER-HOLDER-AGENT business card">
      <div class="brand-row">
        <div class="brand-square" aria-hidden="true"></div>
        <div class="brand-text">
          <div class="brand-name">TRADER - HOLDER - AGENT</div>
          <div class="brand-trades">CARS, CARAVANS, BOATS.</div>
        </div>
      </div>
      <div class="contact-block">
        <p class="contact-mobile">Mobile: 0427591846</p>
        <p class="contact-email">Email: swapnowly@traderholderagent.com.au</p>
        <p class="contact-licence">LMCT-58417</p>
      </div>
      <div class="stripe-orange"></div>
      <div class="stripe-cyan">
        <p class="payment-terms">Cash · Bank Chq · Finance Paid Out</p>
      </div>
    </section>
  </main>
</body>
</html>
```